依頼詳細
石垣島でホテルを経営しておりますのでお土産品として飾って映えるようなかわいらしいパッケージを希望します。箱は紙製です。表面の高さ11cm横10.3cmに入るようにデザインしていただいてもいいですし、箱全体に柄をちりばめてもいいかと思っております。
記載項目
サイズ高さ11cm横幅10.3cm奥行き5cmの和紙風の紙で
横から見ると三角になっています。(写真参考)
希望イメージ
シンプル 複雑
単色 カラフル
暗い 明るい
日常 高級
遊び心 厳粛
未来的 伝統的
女性的 男性的
希望する色
黄・オレンジ系、緑系
納品ファイル
• イラストレーター形式 (.ai)
• PNG形式 (.png)
補足説明
■ 選んだ理由

モロッコの砂漠を連想させる色合いと、今回は文字にもポイントを置いていましたので、文字のデザインもバランスが良かったと思います。エコな感じと素朴な感じが良いと社員みんなに選ばれました。

■ 提案者全員のお礼・コメント

たくさんのご提案があり、驚きました。とても力作ばかりでなかなか一つに絞れませんでした。デザイナーの皆様 本当にありがとうございました。また、次の機会もどうぞよろしくお願いいたします。

```html
<!DOCTYPE html>
<html lang="ja">
<head>
<meta charset="utf-8">
<title>アルガンオイルせっけん パッケージ展開図</title>
<link rel="stylesheet" href="https://fonts.googleapis.com/css2?family=M+PLUS+Rounded+1c:wght@500;800&family=Great+Vibes&display=swap">
<style>
  :root {
    --navy: #1f2a5c;
    --navy-deep: #18214b;
    --teal: #2f8f9c;
    --sky: #6fc3cf;
    --ivory: #fbf7ee;
    --rose: #b8325c;
    --gold: #c7a46a;
    --paper: #ffffff;
  }
  html, body { margin: 0; padding: 0; overflow: hidden; }
  body { width: 877px; height: 1200px; background: var(--paper); position: relative; }
  .panel { position: absolute; }
  .tile-pattern {
    background:
      radial-gradient(circle at 25% 30%, var(--sky) 0 6%, transparent 7%),
      radial-gradient(circle at 75% 70%, var(--sky) 0 6%, transparent 7%),
      linear-gradient(135deg, var(--navy) 0%, var(--teal) 50%, var(--navy) 100%);
    background-size: 60px 60px, 60px 60px, 100% 100%;
  }
  .front { left: 45px; top: 45px; width: 555px; height: 540px; }
  .side-top { left: 615px; top: 90px; width: 235px; height: 495px; background: var(--navy); }
  .side-bottom { left: 615px; top: 655px; width: 235px; height: 500px; background: var(--navy); }
  .back { left: 45px; top: 615px; width: 555px; height: 555px; }
  .back svg { position: absolute; inset: 0; }
  .label {
    position: absolute; left: 195px; top: 50px; width: 240px;
    text-align: center;
  }
  .label svg { position: absolute; left: 0; top: 0; }
  .label-body { position: relative; padding-top: 92px; }
  .cameo {
    position: absolute; left: 100px; top: 30px; width: 40px; height: 48px;
    border-radius: 50% 50% 45% 45%; background: #d9b79a;
  }
  .title {
    font-family: "M PLUS Rounded 1c", sans-serif; font-weight: 800;
    color: var(--rose); font-size: 27px; line-height: 1.3; margin: 0;
  }
  .subtitle {
    font-family: "M PLUS Rounded 1c", sans-serif; font-weight: 800;
    color: var(--navy); font-size: 30px; margin: 30px 0 0; line-height: 1.1;
  }
  .subtitle small { display: block; font-size: 16px; font-weight: 500; margin-top: 4px; }
  .tagline {
    position: absolute; left: 90px; top: 265px; width: 380px; text-align: center;
    font-family: "Great Vibes", cursive; color: var(--gold); font-size: 24px; line-height: 1.35; margin: 0;
  }
</style>
</head>
<body>
  <section class="panel front tile-pattern" role="img" aria-label="ネイビーとターコイズのモロッコタイル柄">
    <div class="label">
      <svg width="240" height="370" viewBox="0 0 240 370" aria-hidden="true">
        <path d="M10 370 V90 Q10 70 40 62 L95 40 Q120 5 145 40 L200 62 Q230 70 230 90 V370 Z"
              fill="var(--ivory)" stroke="var(--gold)" stroke-width="2"/>
      </svg>
      <div class="cameo" role="img" aria-label="女性の横顔シルエット"></div>
      <div class="label-body">
        <h1 class="title">砂漠の風に<br>京娘が<br>ときめいた</h1>
        <p class="subtitle">アルガンオイル<small>が入ったせっけん</small></p>
      </div>
    </div>
  </section>

  <div class="panel side-top"></div>

  <section class="panel back">
    <div class="tile-pattern" style="position:absolute;inset:0;" role="img" aria-label="モロッコタイル柄の帯"></div>
    <svg width="555" height="555" viewBox="0 0 555 555" aria-hidden="true">
      <path d="M0 120 Q0 95 25 95 H530 Q555 95 555 120 V555 H0 Z" fill="var(--navy)"/>
      <path d="M20 215 Q30 200 60 200 H495 Q525 200 535 215" fill="none" stroke="var(--gold)" stroke-width="2"/>
    </svg>
    <p class="tagline">A Kyoto maiden charmed<br>by the desert wind of Morocco</p>
  </section>

  <div class="panel side-bottom"></div>
</body>
</html>
```